Power Washing Business Easy Postcard Design

We need a postcard designed for our company, which does residential power washing. We clean houses, decks, driveways and fences. The design should be understated, high end with minimalist graphics. No bubbles or wild colors. The name of the business is "tallpine power washing" which should be rendered all lower case in a san serif font. Sample files in blue or white are attached. The attached files aren't our logo, just a model. The font doesn't have to be exact and "power washing" needs to be added to it.The postcard size is the Parcel Inkly 8.64" X 5.59". The photo which is attached should fill the whole front of the card.

The text elements on the front are:
1) "tallpine power washing"- as per the attached files, can be broken into two lines

2) "Mention this card and receive a FREE standard size Deck Wash"

3) "804-317-5286"

4) "tallpinepowerwashing.com" (this font size can be smaller than the phone number.)

5)"We Clean:- Houses- Decks- Driveways- Fences"The arrangement is the text is up to you. The text should not overpower the image.

Target Market(s)

Homeowners

Industry/Entity Type

Residential

Font styles to use
Sans Serif

Requirements
Should not have
• Garish graphics

```html
<!DOCTYPE html>
<html lang="en">
<head>
<meta charset="utf-8">
<title>tallpine power washing – postcard</title>
<link rel="stylesheet" href="https://fonts.googleapis.com/css2?family=Arimo:ital,wght@0,400;0,700;1,400&family=Oswald:wght@500;700&display=swap">
<style>
  :root {
    --page: #e9ecef;
    --navy: #0b2a86;
    --navy-dark: #071d63;
    --grass: #8cc63f;
    --white: #ffffff;
    --ink: #111111;
    --red: #e3141b;
    --sky-top: #5f9bea;
    --sky-low: #cfe1f6;
    --house-warm: #c99a5c;
    --house-shade: #5b6170;
  }
  * { margin: 0; padding: 0; box-sizing: border-box; }
  html, body { width: 1200px; height: 779px; overflow: hidden; background: var(--page); }
  .postcard {
    position: absolute; left: 50px; top: 34px; width: 1100px; height: 711px;
    overflow: hidden; background: var(--sky-low);
    font-family: "Arimo", Arial, sans-serif;
  }
  .hero-photo {
    position: absolute; inset: 0;
    background:
      radial-gradient(ellipse 38% 34% at 34% 58%, rgba(240,190,110,.85), rgba(240,190,110,0) 70%),
      linear-gradient(180deg, rgba(0,0,0,0) 55%, rgba(60,110,40,.9) 80%),
      linear-gradient(160deg, var(--sky-top) 0%, var(--sky-low) 45%, var(--house-shade) 70%, var(--house-warm) 100%);
  }
  .shapes { position: absolute; inset: 0; }
  .brand-top {
    position: absolute; left: 52px; top: 48px;
    background: rgba(255,255,255,.88); padding: 10px 22px 12px;
    color: var(--navy-dark); line-height: .9;
  }
  .brand-name { font-weight: 700; font-size: 64px; letter-spacing: -2px; display: block; }
  .brand-sub { font-weight: 400; font-size: 30px; letter-spacing: 1px; display: block; text-transform: uppercase; }
  .call-today {
    position: absolute; left: 40px; top: 540px;
    font-family: "Oswald", "Arial Narrow", sans-serif; font-weight: 700; font-style: italic;
    font-size: 36px; color: var(--white); letter-spacing: 1px;
    -webkit-text-stroke: 1.5px var(--ink); text-transform: uppercase;
  }
  .phone-line { position: absolute; left: 36px; top: 598px; display: flex; align-items: center; gap: 12px; }
  .phone-icon { width: 44px; height: 44px; }
  .phone-number {
    font-family: "Oswald", "Arial Narrow", sans-serif; font-weight: 700;
    font-size: 60px; color: var(--ink); line-height: 1;
  }
  .website {
    position: absolute; left: 92px; top: 666px;
    font-family: "Oswald", "Arial Narrow", sans-serif; font-weight: 500;
    font-size: 28px; line-height: 1.1; color: var(--red); letter-spacing: .5px;
  }
  .safe-note {
    position: absolute; right: 40px; top: 300px; text-align: right;
    font-family: "Oswald", "Arial Narrow", sans-serif; font-weight: 700;
    font-size: 30px; line-height: 1.05; color: var(--white); text-transform: uppercase;
  }
  .services { position: absolute; right: 40px; top: 410px; list-style: none; text-align: right;
    font-family: "Oswald", "Arial Narrow", sans-serif; font-weight: 500; font-size: 28px; color: var(--white); line-height: 1.25; }
  .services li { display: flex; justify-content: flex-end; align-items: center; gap: 8px; }
  .services li:nth-child(2) { margin-right: 20px; }
  .services li:nth-child(3) { margin-right: 40px; }
  .services li:nth-child(4) { margin-right: 60px; }
  .tick { width: 30px; height: 22px; }
  .offer {
    position: absolute; left: 862px; top: 562px; width: 190px; padding: 7px 8px;
    background: var(--white); border: 2px dashed #bbbbbb; transform: rotate(-4deg);
    text-align: center; color: var(--ink); font-family: "Oswald", "Arial Narrow", sans-serif; line-height: 1;
  }
  .offer-lead { font-size: 16px; font-weight: 500; }
  .offer-free { font-size: 52px; font-weight: 700; color: var(--red); }
  .offer-item { font-size: 26px; font-weight: 700; }
  .brand-bottom { position: absolute; left: 600px; top: 560px; color: var(--white); line-height: .9; }
  .brand-bottom .brand-name { font-size: 52px; }
  .brand-bottom .brand-sub { font-size: 24px; }
  .tagline { display: block; margin-top: 6px; font-size: 17px; font-style: italic; font-weight: 400; }
</style>
</head>
<body>
<main class="postcard">
  <div class="hero-photo" role="img" aria-label="Photo of a large two-storey home at dusk with glowing windows, blue sky and a green front lawn"></div>

  <svg class="shapes" width="1100" height="711" viewBox="0 0 1100 711" aria-hidden="true">
    <path d="M0 600 L520 600 C560 540 600 500 640 470 L1100 470 L1100 711 L0 711 Z" fill="var(--grass)"/>
    <path d="M0 594 L520 594 C570 520 640 460 720 420" fill="none" stroke="var(--navy)" stroke-width="10"/>
    <path d="M1100 290 C880 300 700 380 610 500 C580 540 560 580 545 620 L520 711 L1100 711 Z" fill="var(--navy)"/>
  </svg>

  <div class="brand-top">
    <span class="brand-name">tallpine</span>
    <span class="brand-sub">power washing</span>
  </div>

  <p class="call-today">Call us today</p>
  <div class="phone-line">
    <svg class="phone-icon" viewBox="0 0 24 24" aria-hidden="true">
      <rect x="1" y="1" width="22" height="22" rx="4" fill="var(--ink)"/>
      <path d="M8 5c.6 0 1 .3 1.2.8l1 2.4c.2.5 0 1-.3 1.3l-1 .9c.8 1.6 2 2.8 3.6 3.6l.9-1c.3-.4.8-.5 1.3-.3l2.4 1c.5.2.8.7.8 1.2V17c0 1.1-.9 2-2 2C10.3 19 5 13.7 5 7c0-1.1.9-2 2-2z" fill="var(--white)"/>
    </svg>
    <span class="phone-number">804-317-5286</span>
  </div>
  <p class="website">www.TallpinePowerWashing.com</p>

  <p class="safe-note">Safe for<br>environment and<br>landscaping</p>
  <ul class="services">
    <li>Houses <svg class="tick" viewBox="0 0 30 22"><rect x="1" y="4" width="16" height="16" fill="var(--white)"/><path d="M4 11l5 6L28 2" fill="none" stroke="var(--red)" stroke-width="4"/></svg></li>
    <li>Decks <svg class="tick" viewBox="0 0 30 22"><rect x="1" y="4" width="16" height="16" fill="var(--white)"/><path d="M4 11l5 6L28 2" fill="none" stroke="var(--red)" stroke-width="4"/></svg></li>
    <li>Driveways <svg class="tick" viewBox="0 0 30 22"><rect x="1" y="4" width="16" height="16" fill="var(--white)"/><path d="M4 11l5 6L28 2" fill="none" stroke="var(--red)" stroke-width="4"/></svg></li>
    <li>Fences <svg class="tick" viewBox="0 0 30 22"><rect x="1" y="4" width="16" height="16" fill="var(--white)"/><path d="M4 11l5 6L28 2" fill="none" stroke="var(--red)" stroke-width="4"/></svg></li>
  </ul>

  <div class="brand-bottom">
    <span class="brand-name">tallpine</span>
    <span class="brand-sub">power washing</span>
    <span class="tagline">Power &amp; Safe, Effective Cleaning</span>
  </div>

  <div class="offer">
    <div class="offer-lead">Receive a standard size</div>
    <div class="offer-free">FREE</div>
    <div class="offer-item">Deck Wash</div>
  </div>
</main>
</body>
</html>
```